TalkBridge - Language Coaching Services

Sleek, innovative, trendy design for Language Coaching business.

TalkBridge is a new UK based company that provides Language Coaching services. We offer highly personalized on-line and face to face language courses. We also impart learning techniques workshops based on the latest neuroscience research for second-language acquisition.

Target Market(s)

Industry/Entity Type

Consulting

Contact Information for Business Card

TalkBridge
ElenaVT@talkbridge-demo.co.uk
TalkBridge-demo.co.uk
London, UK

Font styles to use
Sans Serif

```html
<!DOCTYPE html>
<html lang="en">
<head>
<meta charset="utf-8">
<title>TalkBridge – Business Card</title>
<link rel="stylesheet" href="https://fonts.googleapis.com/css2?family=Poppins:wght@400;600&display=swap">
<style>
  :root {
    --backdrop: #e9e7e4;
    --card-ink: #2a2829;
    --card-edge: #1fa3dd;
    --brand-blue: #1b95cf;
    --contact-white: #f2f2f2;
  }
  * { box-sizing: border-box; margin: 0; padding: 0; }
  html, body {
    width: 1200px;
    height: 900px;
    overflow: hidden;
    background: var(--backdrop);
    font-family: "Poppins", sans-serif;
  }
  .sheet {
    width: 1200px;
    height: 900px;
    display: flex;
    flex-direction: column;
    align-items: center;
    justify-content: center;
    gap: 40px;
  }
  .card {
    position: relative;
    width: 640px;
    height: 366px;
    background: radial-gradient(ellipse at 50% 40%, #343233 0%, var(--card-ink) 70%);
    border: 10px solid var(--card-edge);
    box-shadow: 0 10px 24px rgba(0, 0, 0, 0.18);
  }
  /* Back of card: contact side */
  .card-back .brand-name {
    position: absolute;
    left: 44px;
    top: 70px;
    font-weight: 600;
    font-size: 22px;
    color: var(--brand-blue);
    letter-spacing: 0.3px;
  }
  .card-back .contact-list {
    position: absolute;
    right: 44px;
    top: 96px;
    list-style: none;
    text-align: right;
    font-weight: 400;
    font-size: 15px;
    line-height: 1.55;
    color: var(--contact-white);
  }
  /* Front of card: wordmark side */
  .card-front .wordmark {
    position: absolute;
    inset: 0;
    display: flex;
    flex-direction: column;
    align-items: center;
    justify-content: center;
    gap: 18px;
  }
  .card-front .wordmark-circle {
    width: 104px;
    height: 104px;
  }
  .card-front .wordmark-name {
    font-weight: 600;
    font-size: 54px;
    letter-spacing: 2px;
    color: var(--brand-blue);
    line-height: 1;
  }
</style>
</head>
<body>
  <main class="sheet">
    <section class="card card-back" aria-label="Business card, contact side">
      <p class="brand-name">TalkBridge</p>
      <ul class="contact-list">
        <li>elenavt@talkbridge-demo.co.uk</li>
        <li>www.talkbridge-demo.co.uk</li>
        <li>London, UK</li>
      </ul>
    </section>

    <section class="card card-front" aria-label="Business card, brand side">
      <div class="wordmark">
        <svg class="wordmark-circle" viewBox="0 0 104 104" aria-hidden="true">
          <circle cx="52" cy="52" r="46" fill="none" stroke="var(--brand-blue)" stroke-width="7"/>
        </svg>
        <p class="wordmark-name">TALKBRIDGE</p>
      </div>
    </section>
  </main>
</body>
</html>
```